Bref créative
Dormly Nest
HMO Specialists
Professional
Rafik Toumi
Partner
We dont want an adress on the business card
Rafik@dormlynest.co.uk
www.dormlynest.co.uk
I Would like to try with HMO Specialists...O
Or
Letting Agency
Or nothing in the subtitle
The Logo

```html
<!DOCTYPE html>
<html lang="en">
<head>
<meta charset="UTF-8">
<title>Dormly Nest – Business Card</title>
<link href="https://fonts.googleapis.com/css2?family=Cinzel:wght@400;600&display=swap" rel="stylesheet">
<style>
  :root {
    --backdrop: #e9e4dc;
    --card: #ffffff;
    --ink: #1d1d1d;
    --brand-green: #5e9a2c;
    --band-green-top: #7cb342;
    --band-green-bottom: #3f7a1c;
    --accent-blue: #3a73b8;
    --divider: #8a8a8a;
  }
  * { margin: 0; padding: 0; box-sizing: border-box; }
  html, body {
    width: 1200px;
    height: 799px;
    overflow: hidden;
    background: var(--backdrop);
    font-family: "Cinzel", "Times New Roman", serif;
    color: var(--ink);
  }
  .business-card {
    position: absolute;
    left: 100px;
    top: 110px;
    width: 1000px;
    height: 580px;
    background: var(--card);
    border-radius: 30px;
    overflow: hidden;
    box-shadow: 0 10px 30px rgba(0,0,0,0.18);
  }
  .brand {
    position: absolute;
    left: 60px;
    top: 250px;
    display: flex;
    align-items: center;
    gap: 18px;
  }
  .brand-dot {
    width: 34px;
    height: 34px;
    border-radius: 50%;
    background: var(--accent-blue);
  }
  .brand-name {
    font-size: 44px;
    font-weight: 600;
    color: var(--brand-green);
    letter-spacing: 1px;
    white-space: nowrap;
  }
  .divider {
    position: absolute;
    left: 520px;
    top: 125px;
    width: 2px;
    height: 320px;
    background: var(--divider);
  }
  .contact-block {
    position: absolute;
    left: 555px;
    top: 140px;
  }
  .person-name {
    font-size: 40px;
    font-weight: 400;
    line-height: 1.1;
  }
  .person-role {
    font-size: 24px;
    margin-top: 6px;
  }
  .contact-list {
    list-style: none;
    margin-top: 58px;
  }
  .contact-item {
    display: flex;
    align-items: center;
    gap: 12px;
    font-size: 26px;
    line-height: 40px;
  }
  .contact-icon {
    width: 22px;
    height: 22px;
    flex: none;
    fill: var(--brand-green);
  }
  .accent-line {
    position: absolute;
    left: 0;
    top: 500px;
    width: 100%;
    height: 6px;
    background: var(--accent-blue);
  }
  .footer-band {
    position: absolute;
    left: 0;
    top: 512px;
    width: 100%;
    height: 68px;
    background: linear-gradient(to bottom, var(--band-green-top), var(--band-green-bottom));
    display: flex;
    align-items: center;
    justify-content: center;
  }
  .website {
    color: #ffffff;
    font-size: 22px;
    letter-spacing: 1px;
  }
</style>
</head>
<body>
  <div class="business-card">
    <div class="brand">
      <span class="brand-dot"></span>
      <span class="brand-name">Dormly Nest</span>
    </div>

    <div class="divider"></div>

    <div class="contact-block">
      <h1 class="person-name">Rafik Toumi</h1>
      <p class="person-role">Partner</p>
      <ul class="contact-list">
        <li class="contact-item">
          <svg class="contact-icon" viewBox="0 0 24 24" aria-hidden="true">
            <path d="M6.6 10.8c1.4 2.8 3.8 5.1 6.6 6.6l2.2-2.2c.3-.3.7-.4 1-.2 1.1.4 2.3.6 3.6.6.6 0 1 .4 1 1V20c0 .6-.4 1-1 1C10.6 21 3 13.4 3 4c0-.6.4-1 1-1h3.5c.6 0 1 .4 1 1 0 1.3.2 2.5.6 3.6.1.3 0 .7-.2 1l-2.3 2.2z"/>
          </svg>
          <span>01632960481</span>
        </li>
        <li class="contact-item">
          <svg class="contact-icon" viewBox="0 0 24 24" aria-hidden="true">
            <path d="M8 1h8c1.1 0 2 .9 2 2v18c0 1.1-.9 2-2 2H8c-1.1 0-2-.9-2-2V3c0-1.1.9-2 2-2zm0 3v14h8V4H8zm4 15.2a1.2 1.2 0 1 0 0 2.4 1.2 1.2 0 0 0 0-2.4z"/>
          </svg>
          <span>07700900318</span>
        </li>
        <li class="contact-item">
          <svg class="contact-icon" viewBox="0 0 24 24" aria-hidden="true">
            <path d="M2 5h20v14H2V5zm2 2v.4l8 5.1 8-5.1V7H4zm16 2.7l-8 5.1-8-5.1V17h16V9.7z"/>
          </svg>
          <span>Rafik@dormlynest.co.uk</span>
        </li>
      </ul>
    </div>

    <div class="accent-line"></div>
    <div class="footer-band">
      <span class="website">www.dormlynest.co.uk</span>
    </div>
  </div>
</body>
</html>
```